Design my dad a new business card because his current one sucks!

I need a business card designed for my fathers home maintenance business. His customers are individuals (single moms, old people etc.) as well as the occasional business. As such it needs to be accessible to both target audiences.

The front of the card should be dark grey on yellow with the logo and contain the following information:
- Warren Dobrinski
- 0487 362 914
- info@harbourlinehandyworks.com.au
- 0487 362 914

- ABN: 87 214 630 592
- 'Fully Insured'

The reverse should be yellow on dark grey and will have the web address:
- harbourlinehandyworks.com.au

And a few key services he offers:
GENERAL REPAIRS
PAINTING/TILING/
PAVING &CONCRETING
PRESSURE WASHING
ON-SITE WELDING
DECKING ADDITIONS & REPAIRS
FENCING
FULL BOND CLEANING

This will be first time the logo has been printed so you will need to come up with the best CMYK approximation of the RGB colours to make sure it is a close as possible.

```html
<!DOCTYPE html>
<html lang="en">
<head>
<meta charset="utf-8">
<title>Harbourline Handyworks – Business Card</title>
<link rel="stylesheet" href="https://fonts.googleapis.com/css2?family=Oxygen:wght@300;400;700&display=swap">
<style>
  :root {
    --yellow: #f5cc14;
    --yellow-light: #fbe24a;
    --yellow-deep: #efb40c;
    --charcoal: #262626;
    --charcoal-light: #3a3a3a;
    --backdrop: #e6e6e6;
    --ink: #2b2b2b;
  }
  * { margin: 0; padding: 0; box-sizing: border-box; }
  html, body {
    width: 1200px;
    height: 873px;
    overflow: hidden;
    background: var(--backdrop);
    font-family: "Oxygen", "Helvetica Neue", Arial, sans-serif;
  }
  .sheet {
    width: 1200px;
    height: 873px;
    display: flex;
    flex-direction: column;
    align-items: center;
    justify-content: center;
    gap: 40px;
  }
  .card {
    position: relative;
    width: 660px;
    height: 377px;
    border-radius: 4px;
    box-shadow: 0 6px 18px rgba(0,0,0,0.18);
    overflow: hidden;
  }
  .card--front {
    background: radial-gradient(ellipse at 55% 40%, var(--yellow-light) 0%, var(--yellow) 45%, var(--yellow-deep) 100%);
    color: var(--ink);
  }
  .card--back {
    background: radial-gradient(ellipse at 50% 40%, var(--charcoal-light) 0%, var(--charcoal) 70%);
    color: var(--yellow);
  }
  .brand {
    position: absolute;
    left: 22px;
    top: 0;
    bottom: 0;
    writing-mode: vertical-rl;
    transform: rotate(180deg);
    text-align: center;
    font-weight: 700;
    font-size: 29px;
    letter-spacing: 0.5px;
    line-height: 1;
  }
  .card--front .brand { color: var(--ink); }
  .card--back .brand { color: var(--yellow); }

  .front-name {
    position: absolute;
    right: 34px;
    top: 34px;
    font-weight: 300;
    font-size: 31px;
  }
  .front-contact {
    position: absolute;
    right: 34px;
    top: 108px;
    text-align: right;
    font-weight: 300;
    font-size: 21px;
    line-height: 1.3;
  }
  .front-tagline {
    position: absolute;
    left: 100px;
    bottom: 28px;
    font-weight: 300;
    font-size: 58px;
    letter-spacing: 0.5px;
  }

  .back-web {
    position: absolute;
    right: 30px;
    top: 30px;
    text-align: right;
    font-weight: 700;
    font-size: 29px;
    line-height: 1.2;
  }
  .services {
    position: absolute;
    right: 30px;
    bottom: 30px;
    list-style: none;
    text-align: right;
    font-weight: 400;
    font-size: 14.5px;
    line-height: 1.32;
    letter-spacing: 0.4px;
    text-transform: uppercase;
  }
</style>
</head>
<body>
  <main class="sheet">
    <section class="card card--front" aria-label="Card front">
      <div class="brand">Harbourline Handyworks</div>
      <p class="front-name">Warren Dobrinski</p>
      <p class="front-contact">
        0487 362 914<br>
        info@harbourlinehandyworks.com.au<br>
        0487 362 914<br>
        ABN: 87 214 630 592
      </p>
      <p class="front-tagline">Fully Insured</p>
    </section>

    <section class="card card--back" aria-label="Card back">
      <div class="brand">Harbourline Handyworks</div>
      <p class="back-web">harbourlinehandyworks<br>.com.au</p>
      <ul class="services">
        <li>General Repairs</li>
        <li>Painting/Tiling/</li>
        <li>Paving &amp;Concreting</li>
        <li>Pressure Washing</li>
        <li>On-Site Welding</li>
        <li>Decking Additions &amp; Repairs</li>
        <li>Fencing</li>
        <li>Full Bond Cleaning</li>
      </ul>
    </section>
  </main>
</body>
</html>
```